Wordpress Theme for Keen Harbor

Template Needs the Following:
-Main Index / home page
-Single post
-Single page
-Archives / All Articles
-Category Archives template
-Sub-Category Archives template
-Header
-Footer
Of course, must be responsive and work on all devices.
Notes on Overall Design
-Color scheme not decided, but prefer a trustworthy blue, maybe a true blue for links and accent color. Mostly black and white.
-Very similar to tobiasfenwick.net in look, style, feel, simplicity, but will have greater focus on images in articles.
-Site is dedicated to long-form, high quality, actionable, evergreen content. This is not a news site, but it will cover a broad variety of topics. Focus on value added over timeliness / 'newness'
-Design ideas are attached as images.
Notes on Single Post Page, Header, and Footer
-For header, Title (Keen Harbor) should be left aligned, far left
-Title can be EITHER image or text. This is a must. Clicking title name / logo should go to keenharborhub.com
-For header, 'Articles', 'About', and 'Premium' can either be center or left aligned with the border of where actual articles can go
-Footer alignment shoot match header alignment (no title needed, though)
-Title should be left aligned
-Category should be link clickable and go to category archives
Home Page / About Page / Single Page
-url is just keenharborhub.com, NOT keenharborhub.com/about
-Same layout as single page layout
-Will be text based, center aligned, very simple
-Includes site header and footer
-Title should be center aligned
-No category or author tags
Main Archives
-3 Featured articles at the top are hand selected by Keen Harbor, NOT the 3 newest articles
-Each Main Category is shown, with a hyperlink to that category's archive page. -Clicking 'More' brings you to this archive as well
-The 3 articles for each main category are text based (no images, to save space), -They are hand selected by Keen Harbor staff, not the most recent articles in the category
-After the category headers, all articles on the entire site are listed by date
Category Archives & Sub-Category Archives
-Same layout as main archives, but with sub-categories where the archives page had categories.
-All articles in that category listed at end of page by date
-Sub-category archives has same layout as main archive and category archive, but with nothing just our 3 favorite articles and all sub category articles by date
1 page

```html
<!DOCTYPE html>
<html lang="en">
<head>
<meta charset="utf-8">
<title>Keen Harbor — Articles</title>
<link rel="stylesheet" href="https://fonts.googleapis.com/css2?family=Lato:wght@400;700&family=Lora:wght@400;700&display=swap">
<style>
  :root {
    --ink: #111111;
    --link: #1c1ad6;
    --rule: #e4e4e6;
    --footer-bg: #eeeef0;
    --page: #ffffff;
  }
  * { box-sizing: border-box; margin: 0; padding: 0; }
  html, body { width: 858px; height: 1200px; overflow: hidden; background: var(--page); }
  body { position: relative; color: var(--ink); font-family: "Lora", Georgia, serif; }
  a { color: var(--link); text-decoration: none; }

  .site-header {
    position: absolute; top: 0; left: 0; width: 858px; height: 49px;
    border-bottom: 1px solid var(--rule);
    font-family: "Lato", Arial, sans-serif;
  }
  .site-title {
    position: absolute; left: 22px; top: 14px;
    font-size: 15px; font-weight: 700; color: var(--ink); letter-spacing: 0.2px;
  }
  .main-nav a {
    position: absolute; top: 20px; font-size: 7.5px; font-weight: 700; color: var(--ink); letter-spacing: 0.3px;
  }
  .nav-articles { left: 340px; }
  .nav-about { left: 412px; }
  .nav-premium { left: 480px; }

  .block { position: absolute; left: 242px; width: 376px; }
  .section-title {
    font-family: "Lato", Arial, sans-serif; font-weight: 700; font-size: 15px; letter-spacing: 0.1px;
  }
  .page-title { text-align: center; }
  .prose { font-size: 9.2px; line-height: 15px; }
  .prose.justified { text-align: justify; }

  .categories { display: flex; }
  .category { position: absolute; top: 0; }
  .category h3 { font-size: 10px; font-weight: 700; margin-bottom: 12px; }
  .category li { list-style: none; font-size: 9.2px; line-height: 16px; white-space: nowrap; }

  .year { font-family: "Lato", Arial, sans-serif; font-size: 14px; font-weight: 700; }
  .archive-list { list-style: none; margin-top: 13px; }
  .archive-list li { display: flex; font-size: 9.2px; line-height: 15px; }
  .archive-list .date { width: 87px; flex: none; }

  .site-footer {
    position: absolute; left: 0; top: 1106px; width: 858px; height: 94px;
    background: var(--footer-bg);
    font-family: "Lato", Arial, sans-serif; font-size: 8px;
    text-align: center; padding-top: 40px;
  }
  .site-footer a { color: var(--ink); }
  .site-footer .sep { margin: 0 5px; }
</style>
</head>
<body>
  <header class="site-header">
    <a class="site-title" href="https://keenharborhub.com">KEEN HARBOR</a>
    <nav class="main-nav">
      <a class="nav-articles" href="#">ARTICLES</a>
      <a class="nav-about" href="#">ABOUT</a>
      <a class="nav-premium" href="#">PREMIUM</a>
    </nav>
  </header>

  <main>
    <h1 class="block section-title page-title" style="top:99px">FAVORITE ARTICLES</h1>
    <p class="block prose" style="top:147px">There are many variations of passages of Lorem Ipsum available, but the majority have suffered alteration in some form, by injected humour, or randomised words which don't look even slightly believable. If you are going to use a passage of Lorem Ipsum, you need to be sure there isn't anything embarrassing hidden in the middle of text. All the Lorem Ipsum generators on the Internet tend to repeat predefined.</p>
    <p class="block prose justified" style="top:244px">It is a long established fact that a reader will be distracted by the readable content of a page when looking at its layout. The point of using Lorem Ipsum is that it has a more-or-less normal distribution of letters, as opposed to using 'Content here, content here', making it look like readable.</p>

    <h2 class="block section-title" style="top:344px;left:243px">3 FAVORITE ARTICLES</h2>
    <p class="block prose" style="top:371px">Browse my Featured articles and essays by category.</p>

    <section class="block" style="top:415px;height:90px">
      <div class="category" style="left:1px">
        <h3>Heading 1</h3>
        <ul>
          <li><a href="#">The point of using Lorem</a></li>
          <li><a href="#">There are many variatio</a></li>
          <li><a href="#">Contrary to popular bel</a></li>
          <li><a href="#">Lorem Ipsum is simply du</a></li>
        </ul>
      </div>
      <div class="category" style="left:140px">
        <h3>Heading 2</h3>
        <ul>
          <li><a href="#">The point of using Lorem</a></li>
          <li><a href="#">There are many variatio</a></li>
          <li><a href="#">Contrary to popular bel</a></li>
          <li><a href="#">Lorem Ipsum is simply du</a></li>
        </ul>
      </div>
      <div class="category" style="left:275px">
        <h3>Heading 3</h3>
        <ul>
          <li><a href="#">The point of using Lorem</a></li>
          <li><a href="#">There are many variatio</a></li>
          <li><a href="#">Contrary to popular bel</a></li>
          <li><a href="#">Lorem Ipsum is simply du</a></li>
        </ul>
      </div>
    </section>

    <h2 class="block section-title" style="top:558px;left:243px">ALL ARTICLES BY DATE</h2>
    <p class="block prose justified" style="top:592px">It is a long established fact that a reader will be distracted by the readable content of a page when looking at its layout. The point of using Lorem Ipsum is that it has a more-or-less normal distribution of letters, as opposed to using 'Content here, content here', making it look like readable.</p>

    <section class="block" style="top:707px;left:243px">
      <h3 class="year">2017</h3>
      <ul class="archive-list">
        <li><span class="date">July 27</span><a href="#">Lorem Ipsum is simply dummy text of the printing</a></li>
        <li><span class="date">June 5</span><a href="#">There are many variations of passages</a></li>
        <li><span class="date">May 15</span><a href="#">search for 'lorem ipsum' will unco</a></li>
        <li><span class="date">May 8</span><a href="#">Contrary to popular belief, Lorem</a></li>
        <li><span class="date">March 29</span><a href="#">unchanged. It was popularised in the 1960s</a></li>
        <li><span class="date">February 13</span><a href="#">more recently with desktop publishin</a></li>
        <li><span class="date">February 6</span><a href="#">Sed ut perspiciatis unde omnis iste</a></li>
        <li><span class="date">January 23</span><a href="#">But I must explain to you how all this mistaken idea</a></li>
        <li><span class="date">January 16</span><a href="#">Denouncing pleasure and praising pain</a></li>
      </ul>
    </section>

    <section class="block" style="top:907px;left:243px">
      <h3 class="year">2016</h3>
      <ul class="archive-list">
        <li><span class="date">July 27</span><a href="#">Lorem Ipsum is simply dummy text of the printing</a></li>
        <li><span class="date">June 5</span><a href="#">There are many variations of passages</a></li>
        <li><span class="date">May 15</span><a href="#">search for 'lorem ipsum' will unco</a></li>
        <li><span class="date">May 8</span><a href="#">Contrary to popular belief, Lorem</a></li>
        <li><span class="date">March 29</span><a href="#">unchanged. It was popularised in the 1960s</a></li>
        <li><span class="date">February 13</span><a href="#">more recently with desktop publishin</a></li>
        <li><span class="date">February 6</span><a href="#">Sed ut perspiciatis unde omnis iste</a></li>
        <li><span class="date">January 23</span><a href="#">But I must explain to you how all this mistaken idea</a></li>
        <li><span class="date">January 16</span><a href="#">Denouncing pleasure and praising pain</a></li>
      </ul>
    </section>
  </main>

  <footer class="site-footer">
    <a href="#">Contact</a><span class="sep">|</span><a href="#">Disclaimer</a><span class="sep">|</span><span>Copyrights @ 2017 All Rights Reserved</span>
  </footer>
</body>
</html>
```